Ablaufgrafik KlickWerkstatt
Zielgruppe
KlickWerkstatt: Content Marketing-Lösung für KMU
Ohne Aufwand verleiht KlickWerkstatt Inhalten (Produkt-Meldungen, Presse-Mitteilungen, Blog-Artikel, …) die notwendige Reichweite um Neukundenkontakte zu generieren.
Der Content geht über alle Kanäle: Web, Mail und Social.
Der KlickWerkstatt bietet flexible und maßgeschneiderte Online Marketing Lösungen, die sich am Bedarf hinsichtlich Quantität, Qualität, den Kunden-Bedürfnissen und dem Budget angleichen. Bis hin zu individuell selektierten Verteilern.
Aufgabenstellung
Es soll eine Ablaufgrafik erstellt werden, die visualisiert "Was passiert mit meinem Content über den KlickWerkstatt": Eine Prozess-Visualisierung.
Die Ablaufgrafik wird als JPG/PNG bei klickwerkstatt.de eingebunden: Mit klick öffnet sich eine bildschirmfüllende Grafik. Ebenso soll die Grafik im factsheet (pdf) eingebunden werden.
- CI gemäß www.klickwerkstatt.de
- Anschauung und Info: factsheet-PDF http://kurzlink-beispiel.de/Rw7TqZ
- Logo: http://kurzlink-beispiel.de/Jm3VbK
Skizze zum Aufbau und den Inhalten für die Ablaufgrafik: s. Dateianlage (pdf)

```html
<!DOCTYPE html>
<html lang="de">
<head>
<meta charset="utf-8">
<title>Ablaufgrafik KlickWerkstatt</title>
<link rel="stylesheet" href="https://fonts.googleapis.com/css2?family=Open+Sans:wght@400;600;700&display=swap">
<style>
  :root{
    --dark:#3c4550;
    --sky:#55c1e0;
    --teal:#5fc0ba;
    --blue:#14a9de;
    --line:#d5d5d5;
    --text:#555a60;
    --white:#ffffff;
  }
  *{margin:0;padding:0;box-sizing:border-box}
  html,body{width:1200px;height:2468px;overflow:hidden;background:var(--white)}
  body{font-family:"Open Sans",Arial,sans-serif;color:var(--text);position:relative}
  .backdrop,.connectors{position:absolute;left:0;top:0}
  .brand{position:absolute;left:102px;top:72px;display:flex;align-items:center;gap:12px}
  .brand-mark{width:40px;height:40px;background:var(--sky)}
  .brand-name{font-size:37px;font-weight:600;color:var(--dark);letter-spacing:-0.5px}
  .step{position:absolute;left:0;width:374px;height:67px;display:flex}
  .step-label{width:295px;background:var(--dark);color:var(--white);font-size:30px;display:flex;align-items:center;justify-content:center}
  .step-label b{font-weight:700;margin-right:8px}
  .step-accent{flex:1;background:var(--sky)}
  .headline{position:absolute;height:57px;display:flex;align-items:center;justify-content:center;
    background:linear-gradient(90deg,var(--teal),var(--blue));color:var(--white);font-size:27px;font-weight:600}
  .node{position:absolute;border:2px solid var(--line);background:var(--white);display:flex;flex-direction:column;
    align-items:center;justify-content:center;text-align:center;font-size:21px;line-height:1.33}
  .node p+p{margin-top:22px}
  .channel{position:absolute;width:164px;height:164px;border-radius:50%;background:var(--sky);color:var(--white);
    display:flex;flex-direction:column;align-items:center;justify-content:center;font-size:28px}
  .channel svg{margin-bottom:6px}
  .analysis{position:absolute;left:493px;top:1699px;width:214px;height:214px;border-radius:50%;background:var(--sky);
    color:var(--white);display:flex;flex-direction:column;align-items:center;justify-content:center;font-size:23px;line-height:1}
  .analysis-visual{width:112px;height:74px;border-radius:6px;background:linear-gradient(135deg,#eef3f6,#f0a27c);margin-bottom:12px;margin-top:-14px}
  .audience{position:absolute;left:224px;top:1993px;display:grid;grid-template-columns:repeat(9,74px);gap:10px 10.4px}
  .person{width:74px;height:74px;border-radius:50%;display:flex;align-items:center;justify-content:center}
  .slogan{position:absolute;left:373px;top:2309px;width:453px;height:62px;border:2px solid var(--line);
    display:flex;align-items:center;justify-content:center;font-size:21px;font-weight:600}
</style>
</head>
<body>

<svg class="backdrop" width="1200" height="640" viewBox="0 0 1200 640" aria-hidden="true">
  <defs>
    <linearGradient id="ringA" x1="0" y1="0" x2="1" y2="0">
      <stop offset="0" stop-color="#8fc8b4"/><stop offset="1" stop-color="#1aa5c2"/>
    </linearGradient>
    <linearGradient id="ringB" x1="0" y1="0" x2="1" y2="1">
      <stop offset="0" stop-color="#93c9b0"/><stop offset="1" stop-color="#5ec6ea"/>
    </linearGradient>
  </defs>
  <circle cx="886" cy="-115" r="292" fill="url(#ringA)"/>
  <circle cx="1197" cy="297" r="311" fill="url(#ringB)" opacity="0.95"/>
  <path d="M1015 38 Q1130 300 1200 470 L1200 0 L1120 0 Q1060 10 1015 38 Z" fill="#0f8fb3" opacity="0.75"/>
</svg>

<svg class="connectors" width="1200" height="2468" viewBox="0 0 1200 2468" aria-hidden="true"
     fill="none" stroke="#d5d5d5" stroke-width="2">
  <path d="M600 354V415M439 415H758M439 415V466M758 415V466"/>
  <path d="M427 454L439 466L451 454M746 454L758 466L770 454"/>
  <path d="M439 532V590M758 532V590M427 578L439 590L451 578M746 578L758 590L770 578"/>
  <path d="M439 657V720H758V657M600 720V771M588 759L600 771L612 759"/>
  <path d="M600 837V894M284 894H917M284 894V940M600 894V940M917 894V940"/>
  <path d="M272 928L284 940L296 928M588 928L600 940L612 928M905 928L917 940L929 928"/>
  <path d="M284 1112V1168M600 1112V1168M917 1112V1168"/>
  <path d="M272 1156L284 1168L296 1156M588 1156L600 1168L612 1156M905 1156L917 1168L929 1156"/>
  <path d="M284 1273V1291M600 1353V1372M600 1435V1454M917 1242V1260M917 1323V1342"/>
  <path d="M284 1353V1560H917V1404M600 1516V1688M588 1676L600 1688L612 1676"/>
  <path d="M600 1913V1982M588 1970L600 1982L612 1970M600 2151V2201M588 2189L600 2201L612 2189"/>
</svg>

<div class="brand"><span class="brand-mark"></span><span class="brand-name">KlickWerkstatt</span></div>

<div class="step" style="top:292px"><div class="step-label"><b>1.</b>ERSTELLEN</div><div class="step-accent"></div></div>
<div class="headline" style="left:488px;top:298px;width:219px">Ihre News</div>
<div class="node" style="left:324px;top:478px;width:176px;height:54px">Mail</div>
<div class="node" style="left:695px;top:478px;width:176px;height:54px">Login</div>
<div class="node" style="left:257px;top:602px;width:243px;height:55px">Einstellerservice</div>
<div class="node" style="left:695px;top:602px;width:264px;height:55px">Redaktionssystem</div>

<div class="step" style="top:778px"><div class="step-label"><b>2.</b>VERBREITEN</div><div class="step-accent"></div></div>
<div class="headline" style="left:482px;top:781px;width:231px">Ihr Newsroom</div>

<div class="channel" style="left:202px;top:948px">
  <svg width="44" height="44" viewBox="0 0 44 44"><path d="M6 4L38 18L24 22L30 38L24 40L18 24L8 32Z" fill="#f6f6f6" stroke="#e06a3c" stroke-width="3" stroke-linejoin="round"/></svg>
  Web
</div>
<div class="channel" style="left:518px;top:948px">
  <svg width="50" height="46" viewBox="0 0 50 46"><rect x="2" y="12" width="46" height="32" fill="#a9dbe9"/><rect x="11" y="2" width="28" height="26" fill="#fff"/><path d="M16 9H34M16 15H34M16 21H30" stroke="#e8774a" stroke-width="2"/><path d="M2 44L25 28L48 44Z" fill="#8fd0e2"/></svg>
  Mail
</div>
<div class="channel" style="left:835px;top:948px">
  <svg width="58" height="42" viewBox="0 0 58 42"><path d="M20 12H56V34H50V40L44 34H20Z" fill="#3c4550"/><path d="M2 2H40V26H14L6 33V26H2Z" fill="#fff"/><path d="M8 9H32M8 15H32M8 20H24" stroke="#55c1e0" stroke-width="2"/></svg>
  Social
</div>

<div class="node" style="left:144px;top:1180px;width:269px;height:93px"><p>Portale<br>im Medien-Netzwerk</p></div>
<div class="node" style="left:144px;top:1291px;width:269px;height:62px">Suchfix &amp; Co.</div>
<div class="node" style="left:465px;top:1180px;width:269px;height:173px"><p>Marketing-Verteiler</p><p>Fach-/führungskräfte,<br>Entscheider,<br>Meinungsmacher, …</p></div>
<div class="node" style="left:465px;top:1372px;width:269px;height:63px">Journalisten-Verteiler</div>
<div class="node" style="left:465px;top:1454px;width:269px;height:62px">Individuelle-Verteiler</div>
<div class="node" style="left:785px;top:1180px;width:269px;height:62px">Freundesbuch</div>
<div class="node" style="left:785px;top:1260px;width:269px;height:63px">Zwitscherdienst</div>
<div class="node" style="left:785px;top:1342px;width:269px;height:62px">Berufsnetz</div>

<div class="step" style="top:1611px"><div class="step-label"><b>3.</b>AUSWERTEN</div><div class="step-accent"></div></div>

<div class="analysis">
  <div class="analysis-visual" role="img" aria-label="Laptop mit Diagrammen und Lupe als Symbol der Auswertung"></div>
  <span>Erfolgs-</span><span>auswertung</span>
</div>

<svg width="0" height="0" style="position:absolute" aria-hidden="true">
  <symbol id="user" viewBox="0 0 40 40"><circle cx="20" cy="14" r="7" fill="none" stroke="#fff" stroke-width="2"/><path d="M6 34Q8 23 20 23Q32 23 34 34Z" fill="none" stroke="#fff" stroke-width="2" stroke-linejoin="round"/></symbol>
</svg>
<div class="audience" aria-label="Neue Kontakte">
  <div class="person" style="background:#5fc0ba"><svg width="38" height="38"><use href="#user"/></svg></div>
  <div class="person" style="background:#57bebd"><svg width="38" height="38"><use href="#user"/></svg></div>
  <div class="person" style="background:#4dbcc1"><svg width="38" height="38"><use href="#user"/></svg></div>
  <div class="person" style="background:#44b9c5"><svg width="38" height="38"><use href="#user"/></svg></div>
  <div class="person" style="background:#3ab6c9"><svg width="38" height="38"><use href="#user"/></svg></div>
  <div class="person" style="background:#30b3cf"><svg width="38" height="38"><use href="#user"/></svg></div>
  <div class="person" style="background:#26b0d5"><svg width="38" height="38"><use href="#user"/></svg></div>
  <div class="person" style="background:#1dacda"><svg width="38" height="38"><use href="#user"/></svg></div>
  <div class="person" style="background:#14a9de"><svg width="38" height="38"><use href="#user"/></svg></div>
  <div class="person" style="background:#5fc0ba"><svg width="38" height="38"><use href="#user"/></svg></div>
  <div class="person" style="background:#57bebd"><svg width="38" height="38"><use href="#user"/></svg></div>
  <div class="person" style="background:#4dbcc1"><svg width="38" height="38"><use href="#user"/></svg></div>
  <div class="person" style="background:#44b9c5"><svg width="38" height="38"><use href="#user"/></svg></div>
  <div class="person" style="background:#3ab6c9"><svg width="38" height="38"><use href="#user"/></svg></div>
  <div class="person" style="background:#30b3cf"><svg width="38" height="38"><use href="#user"/></svg></div>
  <div class="person" style="background:#26b0d5"><svg width="38" height="38"><use href="#user"/></svg></div>
  <div class="person" style="background:#1dacda"><svg width="38" height="38"><use href="#user"/></svg></div>
  <div class="person" style="background:#14a9de"><svg width="38" height="38"><use href="#user"/></svg></div>
</div>

<div class="headline" style="left:482px;top:2211px;width:231px">Ihre Firma</div>
<div class="slogan">Einfach. Erfolgreich. Kunden gewinnen.</div>

</body>
</html>
```